Business Card Design Project

I have had my current business card for 6years and it is time to upgrade my business card. I have uploaded my old card
I am a retail specialty shop designer and want something designer looking but professional.
Target Market(s)
30-60 year old people in retail businesses
Industry/Entity Type
Retail
Requirements
Must have
- The Maple Fitouts logo (but colour can and style can be altered)
My name, position and contact details as per my existing card attached .
Rowan Pellicott Director
m: 0418593417
rowan@maplefitouts-example.com.au
www.maplefitouts-example.com.au
t:02 95318274 f: 02 95318291
po box 871 alexandria nsw 1435
Nice to have
- Use both sides of the card

```html
<!DOCTYPE html>
<html lang="en">
<head>
<meta charset="utf-8">
<title>Maple Fitouts – Business Card</title>
<link rel="stylesheet" href="https://fonts.googleapis.com/css2?family=Arimo:wght@400;700&display=swap">
<style>
  :root {
    --card-deep: #6e2a1e;
    --card-mid: #9a4634;
    --card-warm: #b0603f;
    --band-light: rgba(255, 240, 235, 0.42);
    --ink: #111111;
    --paper: #ffffff;
  }
  html, body {
    margin: 0;
    padding: 0;
    width: 1200px;
    height: 728px;
    overflow: hidden;
    background: #ffffff;
  }
  .card {
    position: relative;
    width: 1200px;
    height: 728px;
    overflow: hidden;
    font-family: "Arimo", Arial, sans-serif;
  }
  .card-texture {
    position: absolute;
    inset: 0;
    background: radial-gradient(ellipse at 55% 45%, var(--card-warm) 0%, var(--card-mid) 45%, var(--card-deep) 100%);
  }
  .brand {
    position: absolute;
    left: 32px;
    top: 338px;
    display: flex;
    align-items: center;
    gap: 14px;
  }
  .brand-square {
    width: 34px;
    height: 34px;
    background: var(--paper);
  }
  .brand-name {
    color: var(--paper);
    font-weight: 400;
    font-size: 40px;
    line-height: 1;
    white-space: nowrap;
  }
  .title-band {
    position: absolute;
    left: 460px;
    top: 264px;
    width: 740px;
    height: 204px;
    background: var(--band-light);
  }
  .contact-band {
    position: absolute;
    left: 0;
    top: 536px;
    width: 1200px;
    height: 140px;
    background: var(--band-light);
  }
  .role {
    position: absolute;
    left: 494px;
    top: 292px;
    margin: 0;
    font-size: 46px;
    font-weight: 400;
    color: var(--ink);
  }
  .person-name {
    position: absolute;
    left: 492px;
    top: 350px;
    margin: 0;
    font-size: 68px;
    font-weight: 700;
    color: var(--ink);
    letter-spacing: -0.5px;
    white-space: nowrap;
  }
  .contact-line {
    position: absolute;
    left: 494px;
    margin: 0;
    font-size: 42px;
    font-weight: 400;
    color: var(--ink);
    white-space: nowrap;
  }
  .contact-mobile { top: 554px; }
  .contact-email { top: 616px; font-size: 38px; }
  .office-details {
    position: absolute;
    left: 32px;
    top: 556px;
    margin: 0;
    font-size: 19px;
    line-height: 34px;
    color: var(--ink);
    white-space: nowrap;
  }
</style>
</head>
<body>
  <div class="card">
    <div class="card-texture" role="img" aria-label="Deep red background with a fine gold honeycomb pattern"></div>

    <div class="brand">
      <span class="brand-square"></span>
      <span class="brand-name">Maple Fitouts</span>
    </div>

    <div class="title-band"></div>
    <p class="role">Director</p>
    <p class="person-name">Rowan Pellicott</p>

    <div class="contact-band"></div>
    <p class="office-details">
      t: 02 95318274&nbsp;&nbsp;f: 02 95318291<br>
      www.maplefitouts-example.com.au<br>
      po box 871 alexandria nsw 1435
    </p>
    <p class="contact-line contact-mobile">m: 0418593417</p>
    <p class="contact-line contact-email">rowan@maplefitouts-example.com.au</p>
  </div>
</body>
</html>
```